Redesign of 2 real estate websites!

We need a redesign of our two real estate websites. These websites offer detailed information on the two real estates and need a modern fresh up.
Both websites should have the same design type, so you can see that they belong together, yet they should be in different colors. There is no logo to these pages, so the headlines can be integreated into the designs.
http://www.korlin-villa.example
http://www.matthias-korlin-haus.example/

Industry/Entity Type

Real Estate

```html
<!DOCTYPE html>
<html lang="de">
<head>
<meta charset="utf-8">
<title>Die Korlin-Villa</title>
<link href="https://fonts.googleapis.com/css2?family=Great+Vibes&family=Oswald:wght@500&family=Arimo:wght@400;700&display=swap" rel="stylesheet">
<style>
:root{
  --green:#022b07;
  --white:#ffffff;
  --grey-band:#ececec;
  --text:#6f6f6f;
  --heading:#555555;
  --field:#ececec;
  --field-line:#d6d6d6;
  --footer:#111111;
  --footer-text:#8a8a8a;
}
*{box-sizing:border-box;margin:0;padding:0}
html,body{width:836px;height:1200px;overflow:hidden}
body{position:relative;background:var(--white);font-family:"Arimo",Arial,sans-serif;color:var(--text)}
.abs{position:absolute}

.site-header{left:0;top:0;width:836px;height:95px;background:var(--green)}
.site-title{left:188px;top:11px;width:460px;height:49px;border:1px solid var(--white);color:var(--white);
  font-family:"Great Vibes",cursive;font-weight:400;font-size:32px;line-height:47px;text-align:center;letter-spacing:1px}
.main-nav a{position:absolute;top:67px;height:27px;line-height:27px;font-family:"Oswald",sans-serif;font-size:10px;
  color:var(--white);text-transform:uppercase;text-decoration:none;white-space:nowrap}
.main-nav a.active{background:var(--white);color:var(--green);width:47px;text-align:center}

.hero{left:0;top:95px;width:836px;height:433px;
  background:linear-gradient(90deg,#3e5a2a 0%,#6d7d55 30%,#b9674e 55%,#c98a70 75%,#9aa98a 100%)}
.hero-caption{left:244px;top:290px;width:348px;height:41px;border:2px solid var(--white);color:var(--white);
  font-size:17px;line-height:37px;text-align:center}

.city{left:0;top:528px;width:836px;height:228px;background:var(--grey-band)}
.section-title{font-size:12.5px;font-weight:700;color:var(--heading)}
.intro-text{font-size:8.4px;line-height:15.4px;color:var(--text)}
.story-text{font-size:8.2px;line-height:14.3px;color:var(--text);text-align:justify}
.story-text p+p{margin-top:14.3px}
.gallery-item{top:610px;width:108px}
.gallery-item .thumb{width:108px;height:76px}
.gallery-item p{margin-top:9px;font-size:8.6px;line-height:11px;text-align:center;color:var(--text)}
.btn{background:var(--green);color:var(--white);font-size:8.5px;text-transform:uppercase;text-align:center;letter-spacing:.3px}

.divider{left:418px;top:770px;width:1px;height:290px;background:#e2e2e2}
.contact-form label{position:absolute;left:427px;font-size:9px;color:var(--heading)}
.field{left:427px;width:334px;background:var(--field);border:1px solid var(--field-line);
  font-size:8.6px;font-style:italic;color:#a9a9a9;padding:5px 6px}

.site-footer{left:0;top:1062px;width:836px;height:138px;background:var(--footer)}
.footer-nav a{position:absolute;top:1076px;font-size:8.6px;color:#c9c9c9;text-decoration:none;white-space:nowrap}
.footer-rule{left:78px;top:1094px;width:681px;height:1px;background:#3a3a3a}
.footer-contact{top:1107px;font-size:7.4px;line-height:9.6px;color:var(--footer-text);padding-left:6px}
.footer-contact.sep{border-left:1px solid #3a3a3a}
.footer-contact strong{color:#bdbdbd}
.copyright{left:0;top:1186px;width:836px;text-align:center;font-size:7.4px;color:#6a6a6a}
</style>
</head>
<body>

<header class="site-header abs">
  <h1 class="site-title abs">Die Korlin-Villa</h1>
</header>
<nav class="main-nav">
  <a class="active" style="left:77px">Home</a>
  <a style="left:140px">Stadt Mühlbach</a>
  <a style="left:232px">Bauentwurf</a>
  <a style="left:306px">Eigentümer &amp; Bewohner</a>
  <a style="left:425px">Die Villa</a>
  <a style="left:486px">Kontakt</a>
  <a style="left:546px">Links / Anfahrt</a>
  <a style="left:636px">Impressum</a>
  <a style="left:702px">Vermietung</a>
</nav>

<div class="hero abs" role="img" aria-label="Foto der Villa mit roter Backsteinfassade, Bäumen und Zaun, Ansicht von der Lindenstraße"></div>
<div class="hero-caption abs">aktuelle Ansicht von der Lindenstrasse</div>

<section class="city abs">
  <h2 class="section-title abs" style="left:78px;top:14px">Allgemeines zur Stadt Mühlbach</h2>
  <p class="intro-text abs" style="left:78px;top:35px;width:680px">Der Landkreis Auental ist ein ländlich gelegener Landkreis im Osten des Landes. Wirtschaftlich betrachtet befindet sich dieser Landkreis in einem Städtedreieck des Umlands mit mehreren größeren Zentren. Er ist industriell und landwirtschaftlich geprägt. Die Kreisstadt ist durch die nahegelegenen Anschlüsse zur Autobahn A00 in alle Richtungen und durch günstige Verbindungen mit Bahn und Bus verkehrsmäßig sehr gut erschlossen.</p>
</section>

<div class="gallery-item abs" style="left:79px"><div class="thumb" role="img" aria-label="Foto: Blick auf die Kirche" style="background:linear-gradient(180deg,#8fb0d6,#7a6a4e)"></div><p>Blick auf die Kirche</p></div>
<div class="gallery-item abs" style="left:193px"><div class="thumb" role="img" aria-label="Luftbild des Marktes" style="background:linear-gradient(160deg,#9c6a52,#b9a68f)"></div><p>Luftbild nach Umbau des Marktes</p></div>
<div class="gallery-item abs" style="left:308px"><div class="thumb" role="img" aria-label="Foto: Marktansicht" style="background:linear-gradient(180deg,#c9d6e2,#b98a62 60%,#8a8178)"></div><p>Marktansicht</p></div>
<div class="gallery-item abs" style="left:422px"><div class="thumb" role="img" aria-label="Foto: Marktansicht mit Ständen" style="background:linear-gradient(180deg,#b8c8d8,#9a7a66 55%,#6f8a6a)"></div><p>Marktansicht</p></div>
<div class="gallery-item abs" style="left:538px"><div class="thumb" role="img" aria-label="Foto: Marktansicht mit Häuserzeile" style="background:linear-gradient(180deg,#9fc0e0,#c79a6e 55%,#a09080)"></div><p>Marktansicht</p></div>
<div class="gallery-item abs" style="left:652px"><div class="thumb" role="img" aria-label="Foto: Blick auf die Stadt" style="background:linear-gradient(180deg,#c2ccd6,#8a6a5a 50%,#5f7a4e)"></div><p>Blick auf Mühlbach</p></div>
<div class="btn abs" style="left:689px;top:719px;width:68px;height:24px;line-height:24px">Mehr</div>

<section>
  <h2 class="section-title abs" style="left:78px;top:771px">Allgemeines zur Stadt Mühlbach</h2>
  <div class="story-text abs" style="left:78px;top:793px;width:330px">
    <p>Aus den Bauzeichnungen für das Wohnhaus ergibt sich, dass die Zeichnungen ursprünglich für den Rentier Theodor Korlin erstellt wurden. Bei den Zeichnungen für die Erweiterungsbauten sind diese offensichtlich von Wilhelm Korlin beauftragt worden. Interessant ist an der Stelle festzustellen, dass sich Wilhelm Korlin bereits damals mit "K" schreibt.</p>
    <p>Vermutlich wurde das Haus Lindenstr. 17 in Mühlbach um die Jahrhundertwende errichtet und später erweitert.</p>
    <p>Soweit bekannt, wohnten in der Lindenstraße 17 von der Erbauerfamilie: Theodor Korlin, Wilhelm Korlin mit seiner Frau und 3 Kindern.</p>
    <p>Schließlich ging das Eigentum an der Lindenstraße 17 an Otto und Greta Korlin (Greta Korlin war eine geb. Edle von Auenfeld) über. Nach dem Tod von Otto Korlin in einem Kurort heiratete Greta Korlin einige Jahre später Konrad Mahrenholz, den ehemaligen Teilhaber eines örtlichen Betriebs in Mühlbach, und zog ins Ausland.</p>
  </div>
  <div class="btn abs" style="left:341px;top:1023px;width:67px;height:25px;line-height:25px">Mehr</div>
</section>

<div class="divider abs"></div>

<section class="contact-form">
  <h2 class="section-title abs" style="left:427px;top:771px">Kontaktformular</h2>
  <label style="top:793px">Name:</label>
  <div class="field abs" style="top:805px;height:24px">Enter Name</div>
  <label style="top:838px">Email:</label>
  <div class="field abs" style="top:850px;height:23px">Enter Email</div>
  <label style="top:881px;left:429px">Betreff:</label>
  <div class="field abs" style="top:892px;height:23px">Enter Text</div>
  <label style="top:923px">Inhalt:</label>
  <div class="field abs" style="top:936px;height:66px">Enter Your Message</div>
  <div class="btn abs" style="left:690px;top:1022px;width:70px;height:24px;line-height:24px">Senden</div>
</section>

<footer class="site-footer abs"></footer>
<nav class="footer-nav">
  <a style="left:92px">Home</a>
  <a style="left:146px">Stadt Mühlbach</a>
  <a style="left:234px">Bauentwurf</a>
  <a style="left:307px">Eigentümer &amp; Bewohner</a>
  <a style="left:426px">die Villa</a>
  <a style="left:487px">Kontakt</a>
  <a style="left:548px">Links / Anfahrt</a>
  <a style="left:632px">Impressum</a>
  <a style="left:703px">Vermietung</a>
</nav>
<div class="footer-rule abs"></div>
<div class="footer-contact abs" style="left:72px;width:170px"><strong>Eigentümer:</strong><br>Grundstücksgesellschaft Lindenstrasse 17 in Mühlbach<br>Marktgasse 4, 01234 Mühlbach<br>Tel.: 0 00 00 / 00 00 00<br>Fax: 0 00 00 / 00 00 01</div>
<div class="footer-contact sep abs" style="left:247px;width:185px">HSB Hausservice Brenner<br>01234 Mühlbach, Neugasse 12<br>Tel.: 0 00 00 / 00 00 02 oder 0 00 / 00 00 03<br>Fax: 0 00 00 / 00 00 04<br>Mobil: 0 00 00 / 00 00 05</div>
<div class="footer-contact sep abs" style="left:436px;width:170px">WKT Immobilien - Gemeinschaftsbüro<br>01234 Mühlbach, Talweg 8<br>Tel.: 0 00 00 / 00 00 06<br>Fax: 0 00 00 / 00 00 07<br>Mobil: 0 00 00 / 00 00 08</div>
<div class="footer-contact sep abs" style="left:605px;width:160px">Seidel Immobilien<br>Herr Paul Seidel<br>01234 Mühlbach, Ahornweg 15<br>Tel.: 0 00 00 / 00 00 09<br>Fax: 0 00 00 / 00 00 10<br>Mobil: 0 00 00 / 00 00 11</div>
<p class="copyright abs">© 2014 Die Korlin-Villa. Alle Rechte vorbehalten.</p>

</body>
</html>
```